I will send the links to the website....I am the Chief Marketing Officer for Doran Vask from TV Shows...Far Drifters, Pair Gone Feral and Solo Legion Unit on Roam Network and Inquiry. Here is the logo background and website. www.doranvaskblades.example

BIO Below

Vask began his career in 1982. He first served on Active Duty, then in Army Reserves and in the National Guard. Vask was a Sergeant First Class (SFC) as a Special Forces Medic (18D), Special Forces Communicator (18E) and Special Forces Operations and Intelligence Sergeant (18F). He recently retired from the U.S. Army Reserves as a Special Forces Captain (18A), also known as a Green Beret Officer. He was assigned in a billet for Major, to U.S. Army Special Forces Command (USASFC) located at Fort Bragg, NC, home of the Green Berets to support 3rd SFGA before he retired in 2010).

As a Sergeant, Vask was a Jump Master, earned numerous foreign jump wings and, for a short period, he was a Recruiter for Special Operations (Psyops and Civil Affairs) in the Reserves. As an SFC, he had attended Infantry (11B) Advance Sergeant School (ANCOC). Vask was also certified as a Paramedic (NR-EMT-PM), Scuba Diver (Tidewater NDRA), and attended training in Skydiving (Ridgeline Freefall Society).

As an Officer, Vask attended Medical Officer School (70B), Infantry Advanced Officer School (11A), and Civil Affairs Advanced Officer School (38A). He also completed the Advanced Officer School and Combined Arms Support Service School (CAS3). While he was a young officer, 2LT, he briefly recruited specialty officers such as Doctors, Lawyers, and Chaplains for the Army Guard.

After 9/11, Vask was a single parent living with his two teen sons and working in L.A. as a Segment Producer for QRN when he was called back to active duty. He spent 2 years serving in the Global War On Terror (GWOT). During this time, he went back through the Special Forces course, sixteen years after the first time, to earn his S.F. Officer Qualification and go on to serve as Commander of the Afghan Militia Forces and later as a Team Commander. He also served as the Executive Officer (XO) for the 18A Committee at the Special Warfare School (SWC) and as an Assistant Operations Officer (S-3a) at 4th Training Battalion (4th BN, SWC.)

During his career as an Officer, Vask also attended some select Special Forces training such as: Anti-Terrorism and Force Protection Instructor (AT/FP Level II), Peace time Government and Hostage Detention (SERE 245, PG-HD), Personnel Recovery (JPRA 102), Survival, Escape, Resistance and Evasion (SERE, Level-C).

As a Reservist, Captain Vask was assigned to support the Active Duty Special Forces unit, 3rd SFGA. Vask is proud to continue to support his S.F. Brethren and sends prayers out for his fallen comrades, their families, and those still serving in harm's way. Doran Vask supports the Elite Veterans League and in a member of his local New Orleans Chapter

Vask runs an adventure training company (www.fieldcraftplus.example) that uses survival for a variety of teaching purposes such as: Corporate Leadership, Family Counseling, Couples Bonding, Singles Mingling, Troubled Teens, Professional Level Safety, Remote Medicine, Elite Military Prep, TV and Film Crew training, Cast and Talent skill provision and advising, Production Company support and development.

Vask began his TV career quite by accident. He started a Medical company to work in War Zones after Desert Storm. The work was intense, so he began a tourism company for his team to get down time working in Costa Rica running children's programs. That's how PLX's Trail Trials Isthmus Tour found FieldCraft and asked Doran to help develop the program for their season finale. Vask ended up representing FieldCraft in a dual role as a bad guy and the good guy on PLX Trail Trials in 1998. He then did some consulting for Nordvik TV in 1999, Grit Barracks in 2000, and Dread Quotient in 2001. After his first TV appearance, he worked on numerous productions as set medic, security, translator, and producer. He was mobilized for two years after 9/11.

Once Vask completed his tour of duty, with the raised profile of Special Forces in the media, he was asked to do a number of other shows as on screen talent. Between 2004-2005 he appeared as a subject matter expert in survival, warfare, leadership, medicine, and special operations for TV shows such as Drills into Daylife, Wellwardens, Albion's Grimmest Gaffer, and Endless Arbor. He appeared in the 2006 movie Grubby Pelham as himself. In 2006, he also filmed an episode of the Inquiry Network's Nobody Walked Out: Physics of Enduring in which he taught survival in the Amazon jungle.

In 2007, he appeared as the Resident Expert on survival for the NBR's series about community survival,Marooned Uncovered, and was featured as a survival camp instructor on The Plain Days Head to Lodge. He appeared as an interrogator and fitness trainer for Felicity Marwood in Rooming with Felicity. In 2008, Vask was a fitness trainer for Brant's Institute in the U.K. and appeared on Orca's Truths Unmasked, Past the Curtain of Lagoon Lodge 2 as the set Medic and Security, which aired in the U.S. A now-frequent guest on Station 9's The Widget Hour, Vask appeared in 2008, demonstrating new survival technologies, and on the show Low Torque, where he was test driving old and new military jeeps. Both shows aired in the U.K.

In 2009, Vask was involved with a new reality series about survival for the Inquiry Network released that spring. He was on the Roam Network's Strange Plates with Dennis Holbrook in June, in which Dennis learned to survive and hunt for his own food in the Mexican jungle. During the summer, he helped out on Brielle & Tamsin Hit Tampa on V+ and was a recurring guest on Glass House After Hours in the U.K. Vask was also on QRN's Sunrise Nation Live with Glen Partridge discussing Family Preparedness in August.

Doran Vask is the creator and star of two hit survival series for the Inquiry Network, Pair, Gone, Feral and Solo Legion Unit. The popular show was not canceled, rather discontinued at Vask's option. He continues to appear on many channels and networks in the US such as the Wallace Penhurst show and Outer Limits Cook and The Widget Hour, Lout Institute and Glass House After Hours in the U.K. With his wife, Petra, Vask currently stars in the Roam Network's series, FAR DRIFTERS, which airs on Tuesdays, 11 PM EST. Doran has a few films in the works, so keep an eye out for those.

Vask was born in Fort Knox, Kentucky and, as an "Army brat," grew up mostly in the southeast in places like: Fort Monroe, VA; Fort Bragg, NC; Fort Benning, GA; Fort Hood; Fort Carson, CO.

He is a 3rd Degree Blackbelt in Aikido and a 1st Degree in Judo. He has also studied Wu Shu and Wing Chun Kung Fu, Karate and Special Forces Combatives. Vask enjoys hiking, camping, shooting, fishing, and all types of outdoor activities as well as teaching, reading, writing, and music. He is an enthusiast in all forms of primitive hunting methods (only for survival food ) as well as having an interest in Native American Knife and Tomahawk fighting techniques.

Vask grew up very poor and survived on the streets as a teen, which is why he is into survival. He was kicked out of junior high school for fighting against bullies, which is why he joined Special Forces to help others. He never attended high school because, as the eldest, he had to take a job to help his mother support his siblings, which is why he is keen on education. He uses his Master's Degree, education, and experience to help others and is pursuing his PhD in order to one day run a full-time camp for kids—his dream job when he retires. If he ever grows up!

Vask is married to TV Presenter Petra Caulfield. They have a son and reside in New Orleans, Louisiana. Vask is also proud to have two grown sons and a grandson and grand daughter living in the U.S. as well.
Updates

We need to remove my address from the business card..and add the following-

www.doranvask.example
www.doranvaskblades.example
www.fieldcraftplus.example

List Two Phone Numbers:
504-555-0148
865-555-0192

Requirements
Must have
• Need to add the following: to the card....
www.doranvask.example
www.doranvaskblades.example
www.fieldcraftplus.example
Nice to have
• We love our background, however do not have access to the files.

```html
<!DOCTYPE html>
<html lang="en">
<head>
<meta charset="utf-8">
<title>Calder Whitlock – Business Card</title>
<link rel="stylesheet" href="https://fonts.googleapis.com/css2?family=Open+Sans:wght@400;600&family=Stardos+Stencil:wght@700&display=swap">
<style>
  :root {
    --backdrop: #1e1e1e;
    --card-olive: #4a4a3a;
    --card-olive-dark: #3b3b2e;
    --card-olive-light: #55553f;
    --band: #1f1f1c;
    --band-edge: #5d5d49;
    --ink: #f2f2ea;
    --ink-soft: #d4d4c8;
    --curl-light: #6a6a52;
    --curl-dark: #3f3f31;
  }
  * { margin: 0; padding: 0; box-sizing: border-box; }
  html, body { width: 1200px; height: 1200px; overflow: hidden; }
  body {
    background: var(--backdrop);
    font-family: "Open Sans", Arial, sans-serif;
    display: flex;
    flex-direction: column;
    align-items: center;
    justify-content: center;
    gap: 40px;
  }
  .card {
    position: relative;
    width: 820px;
    height: 530px;
    overflow: hidden;
    box-shadow: 0 6px 18px rgba(0,0,0,.6);
  }
  .card-texture {
    position: absolute; inset: 0;
    background:
      radial-gradient(ellipse 40% 30% at 25% 30%, var(--card-olive-light), transparent 70%),
      radial-gradient(ellipse 35% 30% at 70% 70%, var(--card-olive-dark), transparent 70%),
      radial-gradient(ellipse 30% 25% at 80% 20%, var(--card-olive-dark), transparent 70%),
      var(--card-olive);
  }
  /* front */
  .band {
    position: absolute;
    top: 228px;
    height: 64px;
    background: var(--band);
    border-bottom: 2px solid var(--band-edge);
  }
  .band-left { left: 0; width: 196px; }
  .band-right { right: 0; width: 204px; }
  .identity {
    position: absolute;
    top: 222px; left: 196px; right: 204px;
    text-align: center;
    color: var(--ink);
  }
  .person-name {
    font-family: "Stardos Stencil", "Georgia", serif;
    font-weight: 700;
    font-size: 39px;
    line-height: 46px;
    letter-spacing: .5px;
  }
  .person-title {
    font-size: 24px;
    font-weight: 400;
    line-height: 30px;
    color: var(--ink-soft);
  }
  .contact {
    position: absolute;
    top: 340px; left: 0; right: 0;
    text-align: center;
    color: var(--ink-soft);
    font-size: 15px;
    line-height: 26px;
  }
  .contact b { font-weight: 600; color: var(--ink); }
  .contact .sep { margin: 0 9px; }
  /* back */
  .curl { position: absolute; inset: 0; }
  .brand-mark {
    position: absolute;
    top: 60px; right: 40px;
    display: flex; align-items: center; gap: 10px;
    color: var(--ink);
    font-family: "Open Sans", Arial, sans-serif;
    font-weight: 600;
    font-size: 18px;
  }
  .brand-mark .dot {
    width: 14px; height: 14px; border-radius: 50%;
    background: var(--ink);
  }
  .back-links {
    position: absolute;
    bottom: 28px; left: 0; right: 0;
    text-align: center;
    color: var(--ink-soft);
    font-size: 14px;
    opacity: .85;
  }
  .back-links .sep { margin: 0 9px; }
</style>
</head>
<body>

  <section class="card card-front">
    <div class="card-texture" role="img" aria-label="Olive camouflage pattern with faint palm tree silhouettes"></div>
    <div class="band band-left"></div>
    <div class="band band-right"></div>
    <div class="identity">
      <h1 class="person-name">CALDER WHITLOCK</h1>
      <p class="person-title">Chief Marketing Officer</p>
    </div>
    <div class="contact">
      <p>418 Fenwick Row Ashdale, TN 37000</p>
      <p><b>P.</b> + 865-555-0192</p>
      <p><b>E.</b> doranvaskblades@mail.example</p>
      <p><b>W.</b> www.doranvask.example<span class="sep">|</span>www.doranvaskblades.example<span class="sep">|</span>www.fieldcraftplus.example</p>
    </div>
  </section>

  <section class="card card-back">
    <div class="card-texture" role="img" aria-label="Olive camouflage pattern"></div>
    <div class="brand-mark"><span class="dot"></span>Doran Vask Blades</div>
    <svg class="curl" viewBox="0 0 820 530" aria-hidden="true">
      <defs>
        <linearGradient id="curlFill" x1="0" y1="0" x2="1" y2="1">
          <stop offset="0" stop-color="var(--curl-dark)"/>
          <stop offset=".55" stop-color="var(--curl-light)"/>
          <stop offset="1" stop-color="var(--curl-dark)"/>
        </linearGradient>
        <filter id="curlShadow" x="-20%" y="-20%" width="140%" height="140%">
          <feDropShadow dx="4" dy="8" stdDeviation="8" flood-color="#000" flood-opacity=".5"/>
        </filter>
      </defs>
      <path d="M380 0 C 400 120, 430 220, 480 282 C 560 210, 680 160, 820 140 L 820 0 Z" fill="none"/>
      <path class="curl-flap" filter="url(#curlShadow)" fill="url(#curlFill)"
            d="M380 0 C 395 110, 425 210, 480 282 C 570 215, 690 175, 780 160 C 640 140, 480 80, 380 0 Z"/>
    </svg>
    <div class="back-links">
      www.doranvask.example<span class="sep">|</span>www.doranvaskblades.example<span class="sep">|</span>www.fieldcraftplus.example
    </div>
  </section>

</body>
</html>
```